Postcard design for Intellectual Property Professional Conference

Seeking design for 5.5" by 8.5" postcard mailer about a conference on tax and finance issues for international IP management. Attendees are lawyers and financial executives. Draft language is attached.

Target Market(s)

The project should have the attached picture of Boston with the caption "Courtesy of the Harborline Meetings & Travelers Council"

Industry/Entity Type

Finance

```html
<!DOCTYPE html>
<html lang="en">
<head>
<meta charset="utf-8">
<title>IP Conference Postcard</title>
<link href="https://fonts.googleapis.com/css2?family=Jost:wght@400;500;600;700&display=swap" rel="stylesheet">
<style>
:root{
  --navy:#10294a;
  --navy-deep:#0a1b33;
  --cyan:#1ea7e6;
  --sky:#8fc0e6;
  --paper:#ffffff;
  --stage:#e8e8e8;
  --grey-photo:#cfcfcf;
  --ink-light:#e8eef6;
}
*{margin:0;padding:0;box-sizing:border-box}
html,body{width:1200px;height:899px;overflow:hidden;background:var(--stage);font-family:"Jost",sans-serif}
.card{position:absolute;width:570px;height:369px;background:var(--paper);box-shadow:0 4px 14px rgba(0,0,0,.18);overflow:hidden}
.card--front{left:15px;top:265px}
.card--back{left:615px;top:265px}

/* front */
.front-head{position:absolute;left:0;top:0;width:100%;height:70px;padding:10px 16px}
.title{color:var(--navy);font-size:23px;font-weight:600;line-height:1}
.subtitle{color:var(--navy);font-size:12.5px;font-weight:500;margin-top:4px;line-height:1.15}
.brand{position:absolute;right:14px;top:12px;display:flex;align-items:center;gap:6px}
.brand-mark{width:12px;height:12px;background:var(--navy);flex:none}
.brand-name{color:var(--navy);font-size:10.5px;font-weight:500;line-height:1.1;white-space:nowrap}
.brand-tag{color:var(--navy);font-size:7px;font-weight:500;margin-top:2px;white-space:nowrap}
.city-photo{position:absolute;left:0;top:70px;width:100%;height:140px;background:linear-gradient(180deg,#6fa6d6 0%,var(--sky) 45%,#b9a58c 75%,#6e5b48 100%)}
.bracket{position:absolute;border:2px solid var(--cyan)}
.bracket--left{left:8px;top:180px;width:14px;height:90px;border-right:none}
.bracket--right{right:8px;top:96px;width:14px;height:90px;border-left:none}
.front-panel{position:absolute;left:0;top:178px;width:100%;height:191px;background:linear-gradient(180deg,rgba(16,41,74,.88) 0%,var(--navy) 22%,var(--navy-deep) 100%)}
.intro{position:absolute;left:26px;top:186px;width:520px;display:flex;gap:14px;color:var(--ink-light);font-size:6.6px;line-height:1.35}
.intro p{flex:1}
.topics-head{position:absolute;left:0;top:244px;width:100%;text-align:center;color:#fff;font-size:8.5px;font-weight:700;letter-spacing:.3px}
.topics{position:absolute;left:20px;top:258px;width:530px;list-style:none;text-align:center;color:var(--ink-light);font-size:5.8px;line-height:1.5}

/* back */
.back-photo{position:absolute;inset:0;background:linear-gradient(180deg,#f4f4f4 0%,#e3e3e3 40%,var(--grey-photo) 75%,#bdbdbd 100%)}
.back .brand{left:236px;top:28px;right:auto}
.stamp-zone{position:absolute;right:14px;top:12px;width:52px;height:60px}
.return-address{position:absolute;right:22px;top:78px;text-align:right;color:var(--navy);font-size:12.5px;font-weight:500;line-height:1.3;font-style:normal}
.speakers{position:absolute;left:22px;top:74px;width:230px;color:var(--navy)}
.speakers h2{font-size:12px;font-weight:600;margin-bottom:3px}
.speakers li{list-style:none;font-size:7.6px;line-height:1.42}
.speakers .more{font-weight:700;font-size:8px;margin-top:4px}
.register{position:absolute;left:18px;top:214px;width:250px;height:124px;background:var(--navy);border-radius:10px;padding:10px 12px;color:#fff}
.register h3{font-size:11.2px;font-weight:600;line-height:1.15;margin-bottom:5px}
.register p{font-size:6.8px;line-height:1.4;color:var(--ink-light)}
.register .link{font-weight:700;color:#fff}
.more-info{position:absolute;right:22px;top:232px;text-align:right;color:var(--navy);font-size:8.3px;line-height:1.45}
.skyline{position:absolute;right:0;bottom:0;width:300px;height:96px;background:linear-gradient(180deg,rgba(30,167,230,.85),var(--cyan))}
</style>
</head>
<body>

<section class="card card--front">
  <div class="city-photo" role="img" aria-label="Photograph of the Boston skyline with harbour and blue sky, courtesy of the Harborline Meetings &amp; Travelers Council"></div>
  <header class="front-head">
    <h1 class="title">Increasing Profits &amp; Protecting</h1>
    <p class="subtitle">Intellectual Property in Developing Growth Markets<br>Boston March 24 &amp; 25, 2016</p>
  </header>
  <div class="brand">
    <span class="brand-mark"></span>
    <div>
      <div class="brand-name">Northgate Cross-Border Markets Association</div>
      <div class="brand-tag">Programs in cross-border tax and legal practice</div>
    </div>
  </div>
  <div class="front-panel"></div>
  <span class="bracket bracket--left"></span>
  <span class="bracket bracket--right"></span>
  <div class="intro">
    <p>You are cordially invited to attend a comprehensive and practical day and a half conference to examine the tax and legal structuring strategies for increasing profits from intellectual property while protecting these important assets when doing business in fast growing developing markets. Intellectual property assets include some of the most important assets of most companies: their patents, trade marks, copyrights, brand names and licensing agreements.</p>
    <p>Senior tax, legal and financial experts will provide a comprehensive analysis of the legal issues, recent tax &amp; regulatory developments, skills and structuring strategies necessary to maximize profits from IP. Migrating IP assets to low tax jurisdictions will also be covered along with dealing with issues of piracy, counterfeiting, infringement and other legal challenges to a company's IP.</p>
  </div>
  <h2 class="topics-head">TOPICS TO BE COVERED INCLUDE:</h2>
  <ul class="topics">
    <li>Market trends in IP tax &amp; legal structures</li>
    <li>Proposed US tax changes and regulatory developments outside the US including European and OECD developments affecting IP, patent box, base erosion and profit shifting (BEPS)</li>
    <li>Overview of the IP landscape in key developing growth markets such as China, India, Brazil, Korea, South Africa, Mexico and other developing markets outside the US</li>
    <li>Legal issues including litigation, arbitration and use of government assistance to protect IP values in key developing markets</li>
    <li>Monetizing IP assets and rights in regard to divestiture, spin offs, M&amp;A, transfers of ownership and associations in developing growth markets</li>
    <li>Special Tax Planning and Legal Considerations for IP in Particular Sectors such as Biopharmaceutical, Information Services Licensing, High Tech, Consumer Brands, and Manufacturing</li>
    <li>Restructuring and Migration of IP Assets to Tax Advantaged Jurisdictions</li>
  </ul>
</section>

<section class="card card--back back">
  <div class="back-photo" role="img" aria-label="Faded greyscale photograph of the Boston waterfront"></div>
  <div class="stamp-zone"></div>
  <div class="brand">
    <span class="brand-mark"></span>
    <div>
      <div class="brand-name">Northgate Cross-Border Markets Association</div>
      <div class="brand-tag">Programs in cross-border tax and legal practice</div>
    </div>
  </div>
  <address class="return-address">NorthgateMarkets.org<br>18 Quarry Lane<br>Ashbury, MA 01799</address>
  <div class="speakers">
    <h2>Speakers</h2>
    <ul>
      <li>Calderon Bio (speaker to be announced)</li>
      <li>Martin Ashby and others (Brandt &amp; Keller)</li>
      <li>Henri L. Marceau, (Whitfield Advisory)</li>
      <li>Daniel Orwell, Pieter Vos, and Anders Lund (Crane Ridley)</li>
      <li>Priya Tandon (Loring Gale)</li>
      <li>Thomas Reed (Stroud Hartley)</li>
      <li>Evan Costa (Hale &amp; Prentiss)</li>
      <li>Lena Park (Barrow Finch)</li>
      <li>Claire Denton (Ashcombe)</li>
    </ul>
    <p class="more">Others to be announced</p>
  </div>
  <div class="register">
    <h3>Seating is limited, we invite you to REGISTER NOW!</h3>
    <p>We look forward to seeing you on Thursday, March 24 at the Boston office of Hale &amp; Prentiss, 9 Harbor Court, Boston, MA 02199<br>
    Register at<br><span class="link">http://www.northgatemarkets.org/ip-conference/attend</span><br>
    Or email<br><span class="link">events@northgatemarkets.org or call 555-014-2290</span></p>
  </div>
  <p class="more-info">Want more information on NCMA or other programs.<br>Send us an email to events@northgatemarkets.org<br>Or send this back with your address</p>
  <div class="skyline" role="img" aria-label="Cyan silhouette of the Boston skyline"></div>
</section>

</body>
</html>
```